Pecan Ridge Paving. Chip Seal Done Right

I need my card to have all my basic information on it. Keep it simple. Include web site, phone number and email address. Include phrase Chip Seal Done Right or Pecan Ridge’s Top Paving Company. Keep card simple. Include color and logo. Put all contact info on card. Make card simple and not complicated.

Here is infuriation yo out in business card

Dale R. Whitmore
830.555.0173 cell phone
Dalewhitmore7@mailbarn.net
www.pecanridgepaving.net

Target Market(s)

Hill Country Texas USA

Industry/Entity Type

Road chip seal

Contact Information for Business Card

We chip seal roads for ranches and property owners

Font styles to use
Serif
Sans Serif
Decorative
Script

Colors
0054AA
0677BA
7BADD7
CADEEF
E8F1F8
EB3D1F
EC4F4E
F09395
F8D3D4
FCEDEE

Requirements
Must have
• Keep it simply
Nice to have
• Logo and all basic info

```html
<!DOCTYPE html>
<html lang="en">
<head>
<meta charset="utf-8">
<title>Pecan Ridge Paving – Business Card</title>
<link rel="stylesheet" href="https://fonts.googleapis.com/css2?family=Montserrat:wght@400;800&family=Arimo:wght@400;700&display=swap">
<style>
  :root {
    --backdrop: #b9b9bb;
    --navy: #1a2050;
    --navy-soft: #232b5e;
    --red: #b01e2d;
    --white: #ffffff;
    --ink: #1b1b1f;
    --ghost: #eeeeef;
  }
  * { box-sizing: border-box; margin: 0; padding: 0; }
  html, body { width: 1200px; height: 900px; overflow: hidden; }
  body { background: var(--backdrop); position: relative; font-family: "Arimo", Arial, sans-serif; }

  .card {
    position: absolute;
    width: 620px; height: 354px;
    border-radius: 26px;
    overflow: hidden;
    box-shadow: 0 6px 14px rgba(0,0,0,.28);
  }
  .card--front { left: 60px; top: 60px; background: var(--navy); }
  .card--back  { left: 520px; top: 486px; background: var(--white); }

  .backdrop-mark { position: absolute; border-radius: 50%; }
  .card--front .backdrop-mark { width: 300px; height: 300px; right: -30px; top: -40px; background: var(--navy-soft); }
  .card--back  .backdrop-mark { width: 300px; height: 300px; right: -30px; top: -60px; background: var(--ghost); }

  .brand { position: absolute; }
  .wordmark { display: flex; align-items: center; gap: 12px; }
  .wordmark__dot { width: 22px; height: 22px; border-radius: 50%; background: var(--red); flex: none; }
  .wordmark__name {
    font-family: "Montserrat", Arial, sans-serif; font-weight: 800;
    text-transform: uppercase; letter-spacing: .5px; line-height: 1; white-space: nowrap;
  }
  .tagline {
    display: flex; align-items: center; justify-content: flex-end; gap: 8px;
    margin-top: 14px;
    font-family: "Montserrat", Arial, sans-serif; font-weight: 400;
    text-transform: uppercase; letter-spacing: 1.5px; color: var(--red); font-size: 11px;
    white-space: nowrap;
  }
  .tagline::before { content: ""; width: 120px; height: 1px; background: var(--red); }

  .card--front .brand { left: 112px; top: 150px; }
  .card--front .wordmark__name { color: var(--white); font-size: 34px; }

  .card--back .brand { left: 40px; top: 58px; }
  .card--back .wordmark__name { color: var(--navy); font-size: 30px; }

  .person { position: absolute; left: 40px; top: 178px; }
  .person__name {
    font-family: "Montserrat", Arial, sans-serif; font-weight: 800;
    color: var(--navy); font-size: 24px; text-transform: uppercase; letter-spacing: .5px;
  }
  .person__role { color: var(--red); font-size: 17px; margin-top: 2px; }

  .contact-list { list-style: none; margin-top: 12px; }
  .contact-list li {
    display: flex; align-items: center; gap: 10px;
    color: var(--ink); font-size: 16px; line-height: 24px; white-space: nowrap;
  }
  .contact-list svg { width: 16px; height: 16px; flex: none; fill: none; stroke: var(--navy); stroke-width: 1.8; }
  .accent { color: var(--red); }

  .address {
    position: absolute; right: 34px; top: 190px;
    text-align: right; color: var(--ink); font-size: 15px; line-height: 22px; font-style: normal;
  }
</style>
</head>
<body>

  <section class="card card--front" aria-label="Card front">
    <div class="backdrop-mark"></div>
    <div class="brand">
      <div class="wordmark">
        <span class="wordmark__dot"></span>
        <span class="wordmark__name">Pecan Ridge Paving</span>
      </div>
      <div class="tagline">Chip Seal Done Right</div>
    </div>
  </section>

  <section class="card card--back" aria-label="Card back">
    <div class="backdrop-mark"></div>
    <div class="brand">
      <div class="wordmark">
        <span class="wordmark__dot"></span>
        <span class="wordmark__name">Pecan Ridge Paving</span>
      </div>
      <div class="tagline">Chip Seal Done Right</div>
    </div>

    <div class="person">
      <h1 class="person__name">Dale R. Whitmore</h1>
      <p class="person__role">Managing Director</p>
      <ul class="contact-list">
        <li>
          <svg viewBox="0 0 16 16"><path d="M4 2l2.5 3-1.5 1.5c.8 1.8 2.2 3.2 4 4L10.5 9l3 2.5-1.5 2.5C7 14 2 9 2 3.5z"/></svg>
          830.555.0173
        </li>
        <li>
          <svg viewBox="0 0 16 16"><rect x="1.5" y="3.5" width="13" height="9"/><path d="M1.5 3.5L8 9l6.5-5.5"/></svg>
          Dalewhitmore7@mailbarn.net
        </li>
        <li>
          <svg viewBox="0 0 16 16"><circle cx="8" cy="8" r="6.5"/><ellipse cx="8" cy="8" rx="2.8" ry="6.5"/><path d="M1.5 8h13"/></svg>
          <span>www.<span class="accent">pecanridgepaving</span>.net</span>
        </li>
      </ul>
    </div>

    <address class="address">
      421 Ridge Bend Road<br>
      Fredericksburg TX 78624
    </address>
  </section>

</body>
</html>
```